Update New Business Card - For Start Up

I need to update my business card, I have our old version for example. I would like to keep to the same colors and theme. We are a threat reporting and case management tool for corporations and educational institutions.

Target Market(s)

Corporate Security and Human Resources, School Administrators and Superintendents.

Industry/Entity Type

Physical Security and Technology.

Contact Information for Business Card

My Name, Founder/CEO, phone number 555-214-6082, Logo, Web...

Colors
0054AA
0677BA
7BADD7
CADEEF
E8F1F8

Requirements
Must have
• Something new and trendy.

```html
<!DOCTYPE html>
<html lang="en">
<head>
<meta charset="utf-8">
<title>Quorvell Business Card</title>
<link href="https://fonts.googleapis.com/css2?family=Exo+2:wght@400;500&family=Montserrat:wght@400;500&display=swap" rel="stylesheet">
<style>
  :root {
    --page: #e4e4e4;
    --charcoal: #2b2c2e;
    --charcoal-light: #36373a;
    --paper: #ffffff;
    --brand-blue: #1f6fb6;
    --name-blue: #1a6cc0;
    --back-deep: #1457a2;
    --back-light: #2b84c3;
    --accent-cyan: #3fe3ff;
    --text-light: #f2f2f2;
  }
  * { margin: 0; padding: 0; box-sizing: border-box; }
  html, body { width: 1200px; height: 1200px; overflow: hidden; }
  body {
    background: var(--page);
    position: relative;
    font-family: "Montserrat", Arial, sans-serif;
  }
  .card {
    position: absolute;
    left: 200px;
    width: 800px;
    height: 456px;
    border-radius: 26px;
    overflow: hidden;
  }
  .card-front { top: 88px; background: var(--paper); }
  .card-back {
    top: 656px;
    background: linear-gradient(30deg, var(--back-deep) 0%, #1c6bb3 55%, var(--back-light) 100%);
  }
  .front-split { position: absolute; inset: 0; }
  .contact-block {
    position: absolute;
    left: 59px;
    top: 136px;
    color: var(--text-light);
  }
  .person-name {
    font-family: "Exo 2", Arial, sans-serif;
    font-weight: 400;
    font-size: 29px;
    color: var(--name-blue);
    line-height: 1;
    letter-spacing: 0.2px;
  }
  .person-title {
    font-size: 18px;
    margin-top: 9px;
    line-height: 1;
  }
  .contact-list { list-style: none; margin-top: 27px; }
  .contact-list li {
    display: flex;
    align-items: center;
    height: 34px;
    font-size: 18.5px;
  }
  .contact-icon { width: 23px; height: 23px; margin-right: 8px; flex: none; }
  .wordmark {
    font-family: "Exo 2", Arial, sans-serif;
    font-weight: 500;
    line-height: 1;
    position: absolute;
    white-space: nowrap;
  }
  .wordmark-front {
    left: 434px;
    top: 224px;
    font-size: 44px;
    letter-spacing: 10px;
    color: var(--brand-blue);
  }
  .back-lockup {
    position: absolute;
    left: 140px;
    top: 175px;
    display: flex;
    align-items: center;
  }
  .back-dot {
    width: 106px;
    height: 106px;
    border-radius: 50%;
    background: var(--accent-cyan);
    margin-right: 16px;
    flex: none;
  }
  .wordmark-back {
    position: static;
    font-size: 54px;
    letter-spacing: 15px;
    color: var(--accent-cyan);
  }
</style>
</head>
<body>

<section class="card card-front">
  <svg class="front-split" width="800" height="456" viewBox="0 0 800 456" aria-hidden="true">
    <defs>
      <linearGradient id="charcoal-fill" x1="0" y1="0" x2="1" y2="1">
        <stop offset="0" stop-color="var(--charcoal-light)"/>
        <stop offset="1" stop-color="var(--charcoal)"/>
      </linearGradient>
    </defs>
    <rect width="800" height="456" fill="url(#charcoal-fill)"/>
    <circle cx="527" cy="237" r="241" fill="var(--paper)"/>
    <rect x="527" width="273" height="456" fill="var(--paper)"/>
  </svg>

  <div class="contact-block">
    <h1 class="person-name">Owen Halvorsen</h1>
    <p class="person-title">Founder/CEO</p>
    <ul class="contact-list">
      <li>
        <svg class="contact-icon" viewBox="0 0 24 24" aria-hidden="true">
          <circle cx="12" cy="12" r="12" fill="var(--name-blue)"/>
          <path d="M8.2 6.3l2 .1 1 2.6-1.3 1.1c.7 1.5 1.7 2.5 3.2 3.2l1.1-1.3 2.6 1 .1 2c-.3 1-1.3 1.6-2.3 1.4-3.8-.8-6.8-3.8-7.6-7.6-.2-1 .4-2 1.2-2.5z" fill="#fff"/>
        </svg>
        555-214-6082
      </li>
      <li>
        <svg class="contact-icon" viewBox="0 0 24 24" aria-hidden="true">
          <circle cx="12" cy="12" r="12" fill="var(--name-blue)"/>
          <rect x="6" y="8" width="12" height="8.5" rx="1" fill="#fff"/>
          <path d="M6.5 8.6l5.5 4.2 5.5-4.2" fill="none" stroke="var(--name-blue)" stroke-width="1.3"/>
        </svg>
        owen@quorvell.co
      </li>
      <li>
        <svg class="contact-icon" viewBox="0 0 24 24" aria-hidden="true">
          <circle cx="12" cy="12" r="12" fill="var(--name-blue)"/>
          <circle cx="12" cy="12" r="5.5" fill="#fff"/>
          <path d="M9.5 8.5c1.5.5 1.2 2 2.5 2.3 1 .3.6 1.8 1.8 2.4M13 16.8c-.2-1.3.8-1.6.3-2.6" fill="none" stroke="var(--name-blue)" stroke-width="1.2"/>
        </svg>
        www.quorvell.co
      </li>
    </ul>
  </div>

  <p class="wordmark wordmark-front">QUORVELL</p>
</section>

<section class="card card-back">
  <div class="back-lockup">
    <span class="back-dot" aria-hidden="true"></span>
    <p class="wordmark wordmark-back">QUORVELL</p>
  </div>
</section>

</body>
</html>
```